Window company.

Hello,

We are a small family business located in Madrid, Spain that works nationwide to fix, change or mount the windows of your home / premises.

The group of possible clients to whom the flyer is focused ranges from 30 to 65 years, families in general who want comfort at home and extra savings every year in heating.

It must include not only graphics and a striking aesthetic in accordance with the concepts of wanting to reach / transmit the final product to the customer to sell the product.

Details to also include:

-Brief history of the company and its foundation in 2006. It will be subsequently translated into Spanish so put in words what you consider necessary so that the client stays with the concept that we are professionals.

--Specialized in exterior aluminum and PVC carpentry.

-We move to your home for a first visit and we provide the budget totally free without any commitment.

- Also payment facilities; up to 3 times, without interest.

-Contact details of the company. (WhatsApp, email, phone and location)
Open: Mon - Friday 11,00am - 9pm
Saturday: 12,00am - 7pm
Sunday: Closed

Also as a suggestion, to decide on your own, graphics of types of window openings, if you consider that anything that is striking for the client so it wonr be yet another advertising flyer.

We are open to all kinds of ideas, all of them involving marketing branding.

We are open to any type of idea and we want to stand out, the construction world is tough and we have an idea to grow, taking into account that it must not only be beautiful but commercial to attract potential customers with all kinds of purchasing power.

Thank you.

```html
<!DOCTYPE html>
<html lang="en">
<head>
<meta charset="utf-8">
<title>Ventanova Windows Flyer</title>
<link rel="stylesheet" href="https://fonts.googleapis.com/css2?family=Roboto:wght@700;900&family=Roboto+Condensed:wght@400;700&display=swap">
<style>
:root{
  --red:#e0202a;
  --white:#ffffff;
  --ink:#1b1b1b;
  --grey-band:#d3d3d3;
  --grey-dark:#a9a9a9;
  --grey-label:#8a8a8a;
  --brand-grey:#5a5a5a;
  --stage:#2a2a2a;
}
*{box-sizing:border-box;margin:0;padding:0}
html,body{width:1200px;height:800px;overflow:hidden}
body{background:var(--stage);font-family:"Roboto Condensed",Arial,sans-serif;color:var(--ink)}
.flyer{position:absolute;left:315px;top:10px;width:570px;height:780px;background:var(--red);overflow:hidden}
.flyer-bg{position:absolute;inset:0}
.seal{position:absolute;left:24px;top:26px;width:96px;height:96px;border-radius:50%;background:var(--ink);border:4px solid var(--white);box-shadow:0 0 0 3px var(--ink)}
.seal-inner{position:absolute;inset:16px;border-radius:50%;background:var(--red)}
.tagline{position:absolute;left:345px;top:38px;width:215px;color:var(--white);font-family:"Roboto",Arial,sans-serif;font-weight:700;font-size:16px;line-height:21px;text-transform:uppercase}
.photo{position:absolute;width:135px;height:140px;border:5px solid var(--white);box-shadow:0 2px 6px rgba(0,0,0,.3)}
.photo-fitter{left:395px;top:121px;background:linear-gradient(135deg,#3d6fa8,#6d6a66 55%,#c9c3bb)}
.photo-handle{left:397px;top:279px;background:linear-gradient(90deg,#d9e4dc,#a6b3a8 40%,#7b5a44 75%,#e4e4e4)}
.photo-team{left:400px;top:442px;background:linear-gradient(180deg,#f2f2f2,#b7c9b0 55%,#3d5a3c)}
.headline{position:absolute;left:35px;top:398px;font-family:"Roboto",Arial,sans-serif;font-weight:900;font-size:28px;line-height:29px;text-transform:uppercase;letter-spacing:-.3px}
.headline .accent{color:var(--red)}
.subhead{position:absolute;left:36px;top:461px;font-size:17px;text-transform:uppercase}
.history{position:absolute;left:36px;top:492px;width:108px;font-size:10px;line-height:11.8px}
.features{position:absolute;left:150px;top:490px;width:240px;list-style:none}
.feature{display:flex;align-items:flex-start;gap:8px;margin-bottom:7px;font-weight:700;font-size:11px;line-height:12px}
.feature-icon{flex:0 0 28px;height:28px;border-radius:50%;background:var(--red);display:flex;align-items:center;justify-content:center;border:2px solid var(--white)}
.feature p{padding-top:2px}
.services{position:absolute;left:152px;top:604px;width:390px;display:flex;flex-wrap:wrap;column-gap:9px;row-gap:2px;list-style:none;font-family:"Roboto",Arial,sans-serif;font-weight:700;font-size:12.5px;text-transform:uppercase}
.services li{display:flex;align-items:center;gap:4px}
.services .tick{width:10px;height:10px}
.cta{position:absolute;left:0;top:648px;width:570px;height:36px;background:var(--red);color:var(--white);display:flex;align-items:center;padding-left:38px;gap:8px;font-size:18px;text-transform:uppercase;white-space:nowrap}
.cta-phone{font-family:"Roboto",Arial,sans-serif;font-weight:900;font-size:18px;display:flex;align-items:center;gap:5px}
.footer{position:absolute;left:0;top:684px;width:570px;height:96px;background:var(--white)}
.brand{position:absolute;left:32px;top:26px;display:flex;align-items:center;gap:10px}
.brand-square{width:42px;height:42px;border:3px solid var(--red)}
.brand-name{font-weight:700;font-size:22px;color:var(--brand-grey);text-transform:uppercase}
.divider{position:absolute;left:206px;top:20px;width:1px;height:58px;background:var(--grey-dark)}
.contact{position:absolute;left:218px;top:20px;list-style:none;font-size:11px;line-height:14px;white-space:nowrap}
.contact li{display:flex;align-items:flex-start;gap:6px}
.contact svg{flex:0 0 10px;margin-top:2px}
.social{position:absolute;left:352px;top:18px;width:56px;text-align:center;font-size:9.5px}
.social-dot{width:38px;height:38px;border-radius:50%;border:3px solid var(--grey-dark);margin:6px auto 0}
.hours{position:absolute;left:412px;top:12px;width:150px;text-align:center;font-size:10.5px;line-height:13px;white-space:nowrap}
.hours-title{display:inline-block;background:var(--grey-label);color:var(--white);font-weight:700;font-size:11px;padding:1px 7px;margin-bottom:4px;text-transform:uppercase}
.hours-closed{color:var(--red);font-weight:700;text-transform:uppercase;margin-top:5px}
</style>
</head>
<body>
<main class="flyer">
  <svg class="flyer-bg" width="570" height="780" viewBox="0 0 570 780">
    <defs>
      <linearGradient id="roomTone" x1="0" y1="0" x2="0" y2="1">
        <stop offset="0" stop-color="#f1f1f1"/>
        <stop offset=".55" stop-color="#dedede"/>
        <stop offset="1" stop-color="#cfcfcf"/>
      </linearGradient>
      <linearGradient id="gardenTone" x1="0" y1="0" x2="0" y2="1">
        <stop offset="0" stop-color="#9fc27a"/>
        <stop offset="1" stop-color="#4f7d3a"/>
      </linearGradient>
    </defs>
    <g role="img" aria-label="Bright empty room with a large white-framed window looking onto a garden">
      <polygon points="0,200 215,20 570,340 570,648 0,648" fill="url(#roomTone)"/>
      <rect x="42" y="140" width="290" height="200" fill="url(#gardenTone)" opacity=".75"/>
    </g>
    <rect x="0" y="482" width="570" height="166" fill="var(--grey-band)"/>
    <polyline points="-10,205 215,16 580,330" fill="none" stroke="var(--white)" stroke-width="26"/>
  </svg>

  <div class="seal" aria-hidden="true"><div class="seal-inner"></div></div>

  <p class="tagline">More comfort at home and extra savings every year in heating</p>

  <div class="photo photo-fitter" role="img" aria-label="Installer fitting a window frame with tools on the sill"></div>
  <div class="photo photo-handle" role="img" aria-label="Hand opening a window by its handle"></div>
  <div class="photo photo-team" role="img" aria-label="Two workers installing a new window"></div>

  <h1 class="headline">We fix, change or<br>mount the <span class="accent">windows</span></h1>
  <p class="subhead">of your home / premises</p>

  <p class="history">Brief history of the company and its foundation in 2006. It will be subsequently translated into Spanish so put in words what you consider necessary so that the client stays with the concept that we are professionals.</p>

  <ul class="features">
    <li class="feature">
      <span class="feature-icon"><svg width="14" height="14" viewBox="0 0 14 14"><path d="M1 7 7 1l6 6M3 6v7h8V6" fill="none" stroke="#fff" stroke-width="1.6"/></svg></span>
      <p>Specialized in exterior aluminum and PVC carpentry.</p>
    </li>
    <li class="feature">
      <span class="feature-icon"><svg width="14" height="14" viewBox="0 0 14 14"><rect x="2" y="1" width="10" height="12" fill="none" stroke="#fff" stroke-width="1.6"/><path d="M4 5h6M4 8h6M4 11h3" stroke="#fff" stroke-width="1.4"/></svg></span>
      <p>We move to your home for a first visit and we provide the budget totally free without any commitment.</p>
    </li>
    <li class="feature">
      <span class="feature-icon"><svg width="14" height="14" viewBox="0 0 14 14"><rect x="1" y="3" width="12" height="8" rx="1" fill="none" stroke="#fff" stroke-width="1.6"/><path d="M1 6h12" stroke="#fff" stroke-width="1.6"/></svg></span>
      <p>Also payment facilities; up to 3 times, without interest.</p>
    </li>
  </ul>

  <ul class="services">
    <li><svg class="tick" viewBox="0 0 12 12"><circle cx="6" cy="6" r="6" fill="var(--red)"/><path d="M3 6l2 2 4-4" fill="none" stroke="#fff" stroke-width="1.6"/></svg>Exterior carpentry</li>
    <li><svg class="tick" viewBox="0 0 12 12"><circle cx="6" cy="6" r="6" fill="var(--red)"/><path d="M3 6l2 2 4-4" fill="none" stroke="#fff" stroke-width="1.6"/></svg>Awnings</li>
    <li><svg class="tick" viewBox="0 0 12 12"><circle cx="6" cy="6" r="6" fill="var(--red)"/><path d="M3 6l2 2 4-4" fill="none" stroke="#fff" stroke-width="1.6"/></svg>Aluminum</li>
    <li><svg class="tick" viewBox="0 0 12 12"><circle cx="6" cy="6" r="6" fill="var(--red)"/><path d="M3 6l2 2 4-4" fill="none" stroke="#fff" stroke-width="1.6"/></svg>Glazing</li>
    <li><svg class="tick" viewBox="0 0 12 12"><circle cx="6" cy="6" r="6" fill="var(--red)"/><path d="M3 6l2 2 4-4" fill="none" stroke="#fff" stroke-width="1.6"/></svg>PVC</li>
    <li><svg class="tick" viewBox="0 0 12 12"><circle cx="6" cy="6" r="6" fill="var(--red)"/><path d="M3 6l2 2 4-4" fill="none" stroke="#fff" stroke-width="1.6"/></svg>Mosquito nets</li>
    <li><svg class="tick" viewBox="0 0 12 12"><circle cx="6" cy="6" r="6" fill="var(--red)"/><path d="M3 6l2 2 4-4" fill="none" stroke="#fff" stroke-width="1.6"/></svg>Skylights</li>
  </ul>

  <div class="cta">
    <span>Call us today to get a free quote</span>
    <span class="cta-phone"><svg width="14" height="20" viewBox="0 0 14 20"><rect x="1.5" y="1.5" width="11" height="17" rx="2" fill="none" stroke="#fff" stroke-width="2"/><circle cx="7" cy="15" r="1.3" fill="#fff"/></svg>34 600 12 34 56</span>
  </div>

  <footer class="footer">
    <div class="brand"><span class="brand-square"></span><span class="brand-name">Ventanova</span></div>
    <span class="divider"></span>
    <ul class="contact">
      <li><svg width="10" height="10" viewBox="0 0 10 10"><circle cx="5" cy="5" r="4" fill="none" stroke="var(--red)" stroke-width="1.4"/></svg>+34 600 12 34 56</li>
      <li><svg width="10" height="10" viewBox="0 0 10 10"><rect x=".7" y="2" width="8.6" height="6" fill="none" stroke="var(--red)" stroke-width="1.3"/><path d="M1 2.5l4 3 4-3" fill="none" stroke="var(--red)" stroke-width="1.2"/></svg>info@ventanova.es</li>
      <li><svg width="10" height="10" viewBox="0 0 10 12"><path d="M5 11S1 6.5 1 4a4 4 0 0 1 8 0c0 2.5-4 7-4 7z" fill="none" stroke="var(--red)" stroke-width="1.4"/><circle cx="5" cy="4" r="1.3" fill="var(--red)"/></svg><span>Pol. Ind. Robledal II<br>Robledal, Spain</span></li>
    </ul>
    <div class="social">Follow Us<div class="social-dot"></div></div>
    <div class="hours">
      <span class="hours-title">Open hours</span>
      <p>Monday- Friday 11,00am - 9pm</p>
      <p>Saturday: 12,00am - 7pm</p>
      <p class="hours-closed">Sunday closed</p>
    </div>
  </footer>
</main>
</body>
</html>
```